Honey Meadow Bake Shop site. I'm opening up a shop in a few months and I have ideas of what I want,

I would like a wordpress design that is mobile friendly. I want to be able to easily add and remove photos when necessary. I want to be able to display my home, about us, contact us, instagram photos, and my menu. I need to eventually include the days and hours the store will be open. I would like to also include the instagram and FB symbol (I know there is a name for it, not sure) that will take you directly to the site.

Please look at the following sites. I like the simplicity of it. I've attached a picture below that shows how I told my logo designer I would like my font.

https://www.cornerplatekitchen.com/
https://www.thebrightcrumbs.com/
http://www.maplelanebakehouse.com/
Below is my instagram page

https://www.instagram.com/honeymeadowbakeshop/

Target Market(s)

All ages

Industry/Entity Type

Bakery

Coding

Coded - Design and coding required

Font styles to use
Serif
Sans Serif

Colors
9d9d9d
757575
474747
fbd4d5

Requirements
Must have
• I've attached my updated logo. Please use it when making the website. Thank you. Keep colors simple. Remember, my bakery is going to have a rustic theme. I've attached my "About Us", please include. I crossed out what I don't want included. Thanks!! :)
Nice to have
• See websites I've attached for ideas. Can't wait to see some designs! Clean borders for pictures, preferably squares. I like the pink, but please, I don't want it to be all you see. Very minimal. I could see some designs without as well. Think rustic chic, simple, elegant. Hope that helps!
Should not have
• I don't want my website to look exactly like the examples. :) No scallop edges. I do not sell online.

```html
<!DOCTYPE html>
<html lang="en">
<head>
<meta charset="utf-8">
<title>Honey Meadow Bake Shop</title>
<link rel="stylesheet" href="https://fonts.googleapis.com/css2?family=Open+Sans:wght@400;600&family=Crimson+Text:wght@400;600&display=swap">
<style>
  :root {
    --blush: #f6e2dc;
    --white: #ffffff;
    --ink: #1d1d1d;
    --sage: #7b9068;
    --sage-text: #7f9670;
    --hero-warm: #3a3129;
    --hero-cool: #474a50;
    --logo-ink: #333333;
  }
  * { box-sizing: border-box; margin: 0; padding: 0; }
  html, body { width: 1200px; height: 705px; overflow: hidden; }
  body { font-family: "Open Sans", Arial, sans-serif; background: var(--white); position: relative; }

  .topbar {
    position: absolute; left: 0; top: 0; width: 1200px; height: 28px;
    background: var(--blush);
    display: flex; justify-content: flex-end; align-items: center;
    padding-right: 121px; gap: 14px;
    font-size: 11px; font-weight: 600; color: var(--ink);
  }
  .topbar .contact-item { display: flex; align-items: center; gap: 3px; }
  .topbar svg { width: 10px; height: 10px; fill: var(--ink); }

  .site-header {
    position: absolute; left: 0; top: 28px; width: 1200px; height: 81px;
    background: var(--white);
  }
  .brand {
    position: absolute; left: 119px; top: 22px;
    display: flex; align-items: center; gap: 8px;
    font-family: "Crimson Text", Georgia, serif; font-size: 26px; font-weight: 400;
    color: var(--logo-ink);
  }
  .brand .mark { width: 14px; height: 14px; border-radius: 50%; background: #f2c9c4; }
  .main-nav {
    position: absolute; right: 121px; top: 30px;
    display: flex; align-items: center;
    font-size: 13px; font-weight: 600; color: var(--ink);
  }
  .main-nav a { color: inherit; text-decoration: none; }
  .main-nav .nav-home { color: var(--sage-text); margin-right: 23px; }
  .main-nav .nav-about { margin-right: 23px; }
  .main-nav .nav-menu { margin-right: 23px; }
  .main-nav .nav-pricing { margin-right: 22px; }
  .main-nav .nav-contact {
    background: var(--sage); color: var(--white);
    width: 101px; height: 29px; border-radius: 3px;
    display: flex; align-items: center; justify-content: center;
  }

  .hero {
    position: absolute; left: 0; top: 109px; width: 1200px; height: 546px;
    overflow: hidden;
  }
  .hero-photo {
    position: absolute; inset: 0;
    background: linear-gradient(90deg, var(--hero-warm) 0%, var(--hero-warm) 45%, var(--hero-cool) 100%);
  }
  .hero-content {
    position: absolute; left: 0; top: 0; width: 1200px; height: 546px;
    display: flex; flex-direction: column; align-items: center;
  }
  .hero-badge {
    margin-top: 145px; width: 128px; height: 128px; border-radius: 50%;
    background: var(--white); border: 1px solid #7a6a64;
    display: flex; align-items: center; justify-content: center; text-align: center;
    font-family: "Crimson Text", Georgia, serif; font-size: 17px; line-height: 1.1;
    color: var(--logo-ink);
  }
  .hero-caption {
    margin-top: 24px; text-align: center;
    font-family: "Crimson Text", Georgia, serif; font-size: 20px; line-height: 20px;
    color: var(--white);
  }
  .hero-cta {
    margin-top: 27px; width: 157px; height: 45px;
    border: 2px solid var(--white); border-radius: 2px;
    display: flex; align-items: center; justify-content: center;
    font-size: 18px; color: var(--white); text-decoration: none;
  }
  .slider-dots {
    position: absolute; left: 566px; top: 506px; display: flex; gap: 9px;
  }
  .slider-dots span { width: 6px; height: 6px; border-radius: 50%; background: rgba(255,255,255,0.5); }
  .slider-dots .active { background: var(--white); }

  .site-footer {
    position: absolute; left: 0; top: 655px; width: 1200px; height: 50px;
    background: var(--sage);
    display: flex; align-items: center; justify-content: space-between;
    padding: 0 121px 0 106px;
    font-size: 13px; color: var(--white);
  }
  .social-links { display: flex; gap: 22px; }
  .social-links span { width: 12px; height: 12px; border-radius: 50%; background: var(--white); display: block; }
</style>
</head>
<body>
  <div class="topbar">
    <span class="contact-item">
      <svg viewBox="0 0 24 24" aria-hidden="true"><path d="M6.6 10.8a15.1 15.1 0 0 0 6.6 6.6l2.2-2.2c.3-.3.7-.4 1-.2 1.1.4 2.3.6 3.6.6.6 0 1 .4 1 1V20c0 .6-.4 1-1 1A17 17 0 0 1 3 4c0-.6.4-1 1-1h3.5c.6 0 1 .4 1 1 0 1.3.2 2.5.6 3.6.1.3 0 .7-.2 1z"/></svg>
      1-888-555-0142
    </span>
    <span class="contact-item">
      <svg viewBox="0 0 24 24" aria-hidden="true"><path d="M2 5h20v14H2z"/><path d="M3 6l9 6 9-6" stroke="var(--blush)" stroke-width="2" fill="none"/></svg>
      hello@honeymeadowbake.com
    </span>
  </div>

  <header class="site-header">
    <div class="brand"><span>Honey Meadow Bake Shop</span><span class="mark"></span></div>
    <nav class="main-nav">
      <a class="nav-home" href="#">Home</a>
      <a class="nav-about" href="#">About Us</a>
      <a class="nav-menu" href="#">Menu</a>
      <a class="nav-pricing" href="#">PRICING</a>
      <a class="nav-contact" href="#">CONTACT US</a>
    </nav>
  </header>

  <section class="hero">
    <div class="hero-photo" role="img" aria-label="Hero photo: a pumpkin pie with decorated crust on a floured slate surface"></div>
    <div class="hero-content">
      <div class="hero-badge">Honey Meadow<br>Bake Shop</div>
      <p class="hero-caption">One of the reasons fall is my favorite time of the year!<br>Love me some pumpkin pie!</p>
      <a class="hero-cta" href="#">Order Now !...</a>
    </div>
    <div class="slider-dots"><span class="active"></span><span></span><span></span><span></span></div>
  </section>

  <footer class="site-footer">
    <p>Copyright © 2017 Honey Meadow Bake Shop.</p>
    <div class="social-links">
      <span aria-label="Social link"></span>
      <span aria-label="Social link"></span>
      <span aria-label="Social link"></span>
      <span aria-label="Feed link"></span>
    </div>
  </footer>
</body>
</html>
```